The Bright Lantern, an online college fair for non-traditional students, needs a web site

I need design and coding for a functioning web site that will serve as an online college fair that connects non-traditional students with college admissions officers and college advisors. I have chosen Wordpress and the "Meridian" theme for the site, and you can see what I already have here: https://brightlanternhub.example/
I need help setting up the site's pages and functionality, including SEO optimization and a password protected area. I will manage all content. In addition to me as the administrator, other users will be: college admissions officers, non-traditional students (like homeschoolers), and college advisors.
Target Market(s)
Homeschoolers and college/university admissions officers
Industry/Entity Type
College
Coding
Coded - Design and coding required
Number of Pages Required
5+ page
Font styles to use
Requirements
Must have
- - An inviting but professional look (see the logo as a starting point)
- - Easy to navigate
- - A way to register subscribed members (students)
- - A password-protected "members only" area
- - Virtual "booths" on the Schools page that lead to a detail page for each school
- - SEO optimized
Nice to have
- - Searchable site

```html
<!DOCTYPE html>
<html lang="en">
<head>
<meta charset="utf-8">
<title>The Bright Lantern</title>
<link href="https://fonts.googleapis.com/css2?family=Oswald:wght@400;500&family=Open+Sans:wght@400;600&display=swap" rel="stylesheet">
<style>
:root{
  --red:#e41b1b;
  --ink:#1c1c1c;
  --muted:#555;
  --light-grey:#efefef;
  --field:#ececec;
  --blush:#fdf0ee;
  --backdrop:#000;
  --white:#fff;
}
*{box-sizing:border-box;margin:0;padding:0}
html,body{width:1200px;height:1119px;overflow:hidden;background:var(--backdrop)}
body{font-family:"Open Sans",sans-serif;color:var(--ink)}
.stage{position:absolute;left:0;top:0;width:1280px;height:1194px;transform:scale(.9375);transform-origin:0 0}
.page{position:absolute;left:434px;top:0;width:412px;height:1194px;background:var(--white);overflow:hidden}
section,header,footer{position:absolute;left:0;width:412px}
.abs{position:absolute}
.heading{font-family:"Oswald",sans-serif;font-weight:500;text-transform:uppercase;letter-spacing:-.2px}
.heading .accent{color:var(--red)}
.copy{font-size:4px;line-height:9px;color:var(--muted)}
.outline-btn{position:absolute;border:1.2px solid var(--red);color:var(--red);font-family:"Oswald",sans-serif;font-size:4.5px;text-align:center;text-transform:uppercase;background:var(--white)}
.photo{position:absolute}

/* header */
.site-header{top:0;height:65px}
.brand{position:absolute;left:160px;top:12px;display:flex;align-items:center;gap:5px}
.brand-mark{width:20px;height:20px;background:var(--red)}
.brand-name{font-family:"Oswald",sans-serif;font-size:8px;font-weight:500;color:var(--ink);text-transform:uppercase;line-height:1}
.main-nav{position:absolute;top:53px;left:0;width:412px;display:flex;justify-content:center;gap:12px;font-size:4.4px;letter-spacing:1px;color:#555;text-transform:uppercase}
.main-nav .current{color:var(--ink);border-bottom:1.2px solid var(--red);padding-bottom:3px}

/* hero */
.hero{top:65px;height:194px}
.hero .photo{inset:0;background:linear-gradient(120deg,#e9ecef 0%,#cfd5da 35%,#f4f4f4 55%,#9aa2aa 100%)}
.slider-btn{position:absolute;top:173px;width:12px;height:12px;display:flex;align-items:center;justify-content:center}
.slider-btn.prev{left:192px;background:#222}
.slider-btn.next{left:207px;background:var(--red)}

/* welcome */
.welcome{top:259px;height:231px}
.welcome .eyebrow{position:absolute;left:28px;top:42px;font-family:"Oswald",sans-serif;font-size:9px;color:#c9c9c9}
.welcome .title{position:absolute;left:28px;top:52px;font-size:17px}
.welcome .frame{position:absolute;left:241px;top:41px;width:156px;height:174px;background:var(--light-grey);padding:7px}
.welcome .frame .photo{position:relative;width:100%;height:100%;background:linear-gradient(135deg,#cfd9e2,#8fa4b8 60%,#e4e8ec)}

/* audiences */
.audiences{top:490px;height:262px;background:var(--blush)}
.audiences .frame{position:absolute;left:29px;top:23px;width:169px;height:173px;background:var(--white);padding:6px}
.audiences .frame .photo{position:relative;width:100%;height:100%;background:linear-gradient(135deg,#3a4458,#7e8797 55%,#c8c6c4)}
.audiences h2{position:absolute;font-size:10px}

/* newsletter */
.newsletter{top:752px;height:143px;background:#1b1b1b}
.newsletter .photo{inset:0;background:linear-gradient(90deg,#141414 0%,#2a2a2a 45%,#5a5550 75%,#3a3835 100%)}
.newsletter h2{position:absolute;left:28px;top:30px;font-size:16px;color:var(--white);font-weight:400}
.newsletter .copy{position:absolute;left:28px;top:59px;width:210px;color:#e8e8e8}
.subscribe{position:absolute;left:28px;top:93px;display:flex}
.subscribe .field{width:140px;height:17px;background:#3b3b3b;color:#bbb;font-size:4px;padding:6px 8px}
.subscribe .send{width:24px;height:17px;background:var(--red);display:flex;align-items:center;justify-content:center}

/* contact */
.contact{top:895px;height:225px}
.contact h2{position:absolute;left:0;width:412px;text-align:center;top:26px;font-size:17px}
.input{position:absolute;background:var(--field);font-size:4px;color:#777;padding:4px 6px}

/* footer band */
.info-band{top:1120px;height:56px;background:var(--red);color:var(--white)}
.phone{position:absolute;left:63px;top:7px;font-size:30px;font-weight:600;letter-spacing:.5px}
.contact-line{position:absolute;left:271px;display:flex;gap:4px;font-size:6.5px;line-height:6.5px}
.legal{top:1176px;height:18px}
.legal p{position:absolute;left:28px;top:7px;font-size:4px;color:#555}
.social{position:absolute;left:326px;top:5px;display:flex;gap:4px}
.social span{width:7px;height:7px}
</style>
</head>
<body>
<div class="stage">
<div class="page">

  <header class="site-header">
    <div class="brand"><span class="brand-mark"></span><span class="brand-name">The Bright Lantern</span></div>
    <nav class="main-nav">
      <span class="current">Home</span><span>Students</span><span>Schools</span><span>Advisors</span><span>Member Resources</span><span>News</span><span>Contact Us</span><span>Login</span>
    </nav>
  </header>

  <section class="hero">
    <div class="photo" role="img" aria-label="Photo of a group of professionals meeting around a bright conference table"></div>
    <span class="slider-btn prev"><svg width="5" height="5" viewBox="0 0 10 10"><path d="M6.5 1.5 3 5l3.5 3.5" stroke="#fff" stroke-width="1.6" fill="none"/></svg></span>
    <span class="slider-btn next"><svg width="5" height="5" viewBox="0 0 10 10"><path d="M3.5 1.5 7 5 3.5 8.5" stroke="#fff" stroke-width="1.6" fill="none"/></svg></span>
  </section>

  <section class="welcome">
    <p class="eyebrow">Welcome To</p>
    <h1 class="heading title">Bright <span class="accent">Lantern</span></h1>
    <p class="copy abs" style="left:28px;top:86px;width:205px">Bright Lantern is an online college fair built for students who learn outside the usual path. Meet admissions officers, compare schools and find advisors who understand your story.</p>
    <p class="copy abs" style="left:28px;top:122px;width:205px">Members can visit school booths, join live webinars and read guides on admissions, financial aid and transcripts for homeschoolers. Colleges meet motivated applicants, and advisors share expertise with families. Join free today and start planning your next step with clear, friendly help from people who care about your success.</p>
    <span class="outline-btn" style="left:28px;top:191px;width:60px;height:16px;line-height:14px">Login</span>
    <div class="frame"><div class="photo" role="img" aria-label="Photo of colleagues discussing work at a table"></div></div>
  </section>

  <section class="audiences">
    <div class="frame"><div class="photo" role="img" aria-label="Photo of a student drinking from a mug while working at a laptop"></div></div>
    <h2 class="heading" style="left:206px;top:22px">For <span class="accent">Students</span></h2>
    <p class="copy abs" style="left:206px;top:42px;width:178px">Free membership for any student or parent who wants to learn more about the colleges and universities that are actively recruiting non-traditional students, all in one location. You will have access to admissions officers, independent advisors, helpful articles, resource reviews and links. We also offer regular events like webinars and panels, where you can connect directly with college staff and students from similar backgrounds as you prepare to apply.</p>
    <h2 class="heading" style="left:206px;top:117px">For Colleges <span class="accent">and Universities</span></h2>
    <p class="copy abs" style="left:206px;top:136px;width:172px">An audience of thousands of non-traditional students who want to hear about your school and programs. You will have a dedicated page to set up a virtual booth, or school profile, where you can describe your institution, highlight programs that appeal to non-traditional students, offer details of your admissions process and requirements, and provide contact information.</p>
    <h2 class="heading" style="left:28px;top:210px">For Independent <span class="accent">College Advisors</span></h2>
    <p class="copy abs" style="left:28px;top:227px;width:356px">A platform for sharing your services and connecting with thousands of students who need your guidance. Through forums, articles, ads and online events, there will be multiple opportunities to share your knowledge and expertise, and to work closely with individual students.</p>
  </section>

  <section class="newsletter">
    <div class="photo" role="img" aria-label="Photo of a student wearing headphones working at a laptop in a dim room"></div>
    <h2 class="heading">Newsletter</h2>
    <p class="copy">Sign up for news on upcoming fairs, webinars and school booths, sent to your inbox once a month.</p>
    <div class="subscribe">
      <span class="field">Email</span>
      <span class="send"><svg width="8" height="8" viewBox="0 0 12 12"><path d="M1 6 11 1 8 11 6 7Z M6 7 11 1" stroke="#fff" stroke-width="1" fill="none" stroke-linejoin="round"/></svg></span>
    </div>
  </section>

  <section class="contact">
    <h2 class="heading">Contact <span class="accent">Us</span></h2>
    <span class="input" style="left:50px;top:72px;width:150px;height:17px">Name</span>
    <span class="input" style="left:213px;top:72px;width:150px;height:17px">Email</span>
    <span class="input" style="left:50px;top:95px;width:313px;height:16px">Subject</span>
    <span class="input" style="left:50px;top:115px;width:313px;height:62px">Comments</span>
    <span class="outline-btn" style="left:175px;top:191px;width:60px;height:16px;line-height:14px">Submit</span>
  </section>

  <footer class="info-band">
    <p class="phone">555 010 4477</p>
    <p class="contact-line" style="top:15px"><svg width="7" height="6" viewBox="0 0 14 11"><rect x="1" y="1" width="12" height="9" fill="none" stroke="#fff" stroke-width="1.4"/><path d="M1 1 7 6 13 1" fill="none" stroke="#fff" stroke-width="1.4"/></svg>hello@brightlantern.example</p>
    <p class="contact-line" style="top:27px"><svg width="6" height="8" viewBox="0 0 10 14"><path d="M5 13C2 9 1 7 1 5a4 4 0 0 1 8 0c0 2-1 4-4 8Z" fill="none" stroke="#fff" stroke-width="1.4"/><circle cx="5" cy="5" r="1.5" fill="#fff"/></svg><span>1420 harbor lane<br>alder bay, CA 90000</span></p>
  </footer>

  <footer class="legal">
    <p>Copyright © 2017 Bright Lantern. All rights reserved</p>
    <div class="social" aria-label="Social links">
      <span style="background:#f2b53a"></span><span style="background:#3fa9e0"></span><span style="background:#d9579c"></span><span style="background:#59c0e8"></span><span style="background:#3b5998"></span>
    </div>
  </footer>

</div>
</div>
</body>
</html>
```